Plakat-Design für Kindergarten
Zielgruppe
Wir sind ein kleiner, sehr familiärer Kindergarten 'Sonnenwiese'.
Wir suchen für 2020 eine Kinderpflegerin oder Erzieherin.
Unsere Zielgruppe sind Leute mit Freude an der Arbeit mit Kindern.
Wir machen sehr viele Ausflüge.
Aufgabenstellung
Auffälligkeit. Soll sich unter vielen Stellenanzeigen hervorheben.
Es soll auf eine coole Arbeitstelle Interesse wecken.
Bunt mit STILVOLLEN Farben und fröhlich.
Keine Fotos, lieber Zeichnungen oder Grafiken.
Vorhandenes Logo muss nicht unbedingt eingebunden werden. Dient nur als Info.
Bitte keine Anlehnung an unsere Homepage (die ist nämlich schrecklich...)

```html
<!DOCTYPE html>
<html lang="de">
<head>
<meta charset="utf-8">
<title>Stellenplakat Kindergarten Sonnenwiese</title>
<link rel="stylesheet" href="https://fonts.googleapis.com/css2?family=Amatic+SC:wght@400;700&display=swap">
<style>
  :root {
    --paper: #ece6dc;
    --paper-dark: #e3dccf;
    --cloud: #ffffff;
    --cloud-shadow: #cbc4b9;
    --teal: #88b5aa;
    --teal-dark: #6f968b;
    --ink: #7fb0a3;
    --light: #ffffff;
  }
  * { margin: 0; padding: 0; box-sizing: border-box; }
  html, body { width: 881px; height: 1200px; overflow: hidden; background: var(--paper); }
  .poster {
    position: relative;
    width: 881px; height: 1200px;
    background: radial-gradient(ellipse at 50% 30%, var(--paper) 0%, var(--paper-dark) 100%);
    font-family: "Amatic SC", cursive;
    overflow: hidden;
  }
  .poster-art { position: absolute; inset: 0; }
  .headline {
    position: absolute; left: 0; right: 0; top: 250px;
    text-align: center; color: var(--ink);
  }
  .headline .intro { font-size: 24px; font-weight: 700; letter-spacing: 0.5px; line-height: 1; }
  .headline .role { font-size: 100px; font-weight: 700; line-height: 0.9; margin-top: 22px; }
  .headline .or { font-size: 24px; line-height: 1; margin: 8px 0 6px; }
  .contact {
    position: absolute; top: 1072px;
    color: var(--light); font-size: 31px; line-height: 1.3; font-weight: 400;
  }
  .contact-apply { left: 60px; }
  .contact-address { left: 618px; display: flex; gap: 8px; align-items: flex-start; }
  .contact-address svg { margin-top: 4px; }
</style>
</head>
<body>
<main class="poster">
  <svg class="poster-art" width="881" height="1200" viewBox="0 0 881 1200">
    <!-- illustrated playground scene area -->
    <rect class="scene-illustration" x="0" y="600" width="881" height="390" rx="30"
          fill="url(#sceneTones)" role="img"
          aria-label="Aquarell-Illustration: zwei spielende Kinder, Luftballons, Wolken und Blumen"/>
    <defs>
      <linearGradient id="sceneTones" x1="0" y1="0" x2="1" y2="1">
        <stop offset="0" stop-color="#d5dde0" stop-opacity="0.8"/>
        <stop offset="0.4" stop-color="#e6d6bf" stop-opacity="0.7"/>
        <stop offset="1" stop-color="#e3b99a" stop-opacity="0.6"/>
      </linearGradient>
    </defs>

    <!-- cloud title shape with shadow -->
    <g class="title-cloud-shadow" fill="var(--cloud-shadow)" transform="translate(12 10)">
      <circle cx="440" cy="280" r="140"/>
      <circle cx="440" cy="555" r="140"/>
      <circle cx="300" cy="418" r="145"/>
      <circle cx="580" cy="418" r="145"/>
      <rect x="300" y="280" width="280" height="275"/>
    </g>
    <g class="title-cloud" fill="var(--cloud)">
      <circle cx="440" cy="280" r="140"/>
      <circle cx="440" cy="555" r="140"/>
      <circle cx="300" cy="418" r="145"/>
      <circle cx="580" cy="418" r="145"/>
      <rect x="300" y="280" width="280" height="275"/>
    </g>

    <!-- dashed flight paths -->
    <g fill="none" stroke="var(--light)" stroke-width="2" stroke-dasharray="7 6">
      <path d="M140 282 Q190 260 240 248"/>
      <path d="M760 540 Q790 538 800 520"/>
      <path d="M0 1075 Q80 1070 120 1020"/>
    </g>

    <!-- butterfly badge -->
    <g class="badge-butterfly">
      <circle cx="115" cy="242" r="48" fill="var(--teal-dark)" opacity="0.9"/>
      <path d="M112 232 q-14 -16 -20 4 q14 6 20 0 q8 20 22 6 q2 -18 -22 -10" fill="none" stroke="var(--light)" stroke-width="2.5" stroke-linecap="round"/>
    </g>

    <!-- pencil badge -->
    <g class="badge-pencil">
      <ellipse cx="810" cy="513" rx="45" ry="62" transform="rotate(18 810 513)" fill="var(--teal-dark)" opacity="0.9"/>
      <g fill="none" stroke="var(--light)" stroke-width="2.5" stroke-linejoin="round" transform="rotate(20 810 513)">
        <rect x="800" y="480" width="20" height="58"/>
        <path d="M800 480 l10 -18 l10 18"/>
        <line x1="800" y1="530" x2="820" y2="530"/>
      </g>
    </g>

    <!-- meadow band -->
    <path class="meadow" fill="var(--teal)"
          d="M0 950 Q60 900 150 925 Q230 880 330 920 Q420 880 500 925 Q580 890 660 915 Q740 890 800 920 Q850 905 881 925 L881 1200 L0 1200 Z"/>

    <!-- paper plane badge -->
    <g class="badge-plane">
      <circle cx="182" cy="980" r="70" fill="var(--teal-dark)"/>
      <g fill="none" stroke="var(--light)" stroke-width="3" stroke-linejoin="round">
        <path d="M140 990 L225 945 L190 1015 Z"/>
        <path d="M225 945 L165 1000 L172 1022 L182 1005"/>
      </g>
    </g>
  </svg>

  <header class="headline">
    <p class="intro">wir suchen für 2020 eine</p>
    <h1 class="role">Kinderpflegerin</h1>
    <p class="or">oder</p>
    <h1 class="role">Erzieherin</h1>
  </header>

  <p class="contact contact-apply">Bewerbungen an:<br>info@sonnenwiese-kiga.de</p>
  <div class="contact contact-address">
    <svg width="26" height="34" viewBox="0 0 26 34" aria-hidden="true">
      <path d="M13 32 C4 20 2 16 2 12 A11 11 0 0 1 24 12 C24 16 22 20 13 32 Z" fill="none" stroke="var(--light)" stroke-width="2"/>
      <circle cx="13" cy="12" r="4" fill="none" stroke="var(--light)" stroke-width="2"/>
    </svg>
    <p>Wiesenstr. 42<br>80999 München-Allach</p>
  </div>
</main>
</body>
</html>
```